Facebook Velarte9 to attract customers

We need a Facebook design that brings seriousness and professionalism in the field of business advice. We enclose the logo that a colleague of yours designed in Pixelmora.
The company is called: Velarte9 Asesoría y Administración de Empresas, but the commercial name is Velarte9.
We are dedicated to advising companies, providing the following services: tax, labor, accounting, administration and finance.
We would like a design that respects the colors of the attached logo, we also attach the logo in black and white, in case you need it for an image. The design, as we have already said, must communicate security, trust, professionalism and also be attractive for sale, that is, that customers who visit Facebook are attracted to ask for information, call, or give "like" in the page.
The client profile we are looking for are companies and freelancers.

Target Market(s)

Companies and freelancers in Spain

Industry/Entity Type

Asesoría de empresas, Consultoría

Font styles to use
Sans Serif

Colors
0054AA
0677BA
7BADD7
CADEEF
E8F1F8

Requirements
Must have
• We are a business consultancy so it must convey seriousness, professionalism, trust and that encourages being sold, that is, those who agree contact us or like the page
Nice to have
• Create a cover photo, that the services appear (Tax, Labor, Accounting, Administration and Financial), profile image (we have attached the logo if it is worth it), contact forms and access to quick likes. It is very important that it is compatible with the SEO and SEM of the company. We also seek to design a kind of "template" for our publications, making sure that each time we publish a format and an image are followed and we are recognized just by seeing the publication

```html
<!DOCTYPE html>
<html lang="es">
<head>
<meta charset="utf-8">
<title>Velarte9 – Portada</title>
<link href="https://fonts.googleapis.com/css2?family=Montserrat:wght@400;500;600;700;800&display=swap" rel="stylesheet">
<style>
  :root{
    --brand-blue:#0054AA;
    --brand-mid:#0677BA;
    --brand-light:#7BADD7;
    --brand-pale:#CADEEF;
    --brand-mist:#E8F1F8;
    --navy:#0d1f3c;
    --accent-yellow:#F2E600;
    --white:#ffffff;
    --page-bg:#eef1f5;
  }
  html,body{margin:0;padding:0;width:1200px;height:767px;overflow:hidden;background:var(--page-bg);}
  .canvas{display:block;width:1200px;height:767px;font-family:'Montserrat',sans-serif;}
  .headline{font-weight:800;font-size:54px;letter-spacing:-2.5px;}
  .headline .light{font-weight:500;letter-spacing:-1px;}
  .headline .accent{fill:var(--accent-yellow);}
  .lead{font-weight:500;font-size:14px;fill:var(--white);}
  .phone-number{font-weight:800;font-size:29px;fill:var(--accent-yellow);}
  .service-label{font-weight:500;font-size:11px;fill:var(--white);letter-spacing:.2px;}
  .contact-text{font-weight:800;font-size:16.5px;fill:var(--brand-blue);}
  .brand-name{font-weight:700;fill:var(--brand-blue);}
  .brand-tagline{font-weight:500;fill:var(--brand-mid);}
</style>
</head>
<body>
<svg class="canvas" viewBox="0 0 1200 767" xmlns="http://www.w3.org/2000/svg">
  <defs>
    <linearGradient id="coverBlue" x1="0" y1="0" x2="1" y2="1">
      <stop offset="0" stop-color="#0a4fa6"/>
      <stop offset="1" stop-color="#0b3f8f"/>
    </linearGradient>
    <radialGradient id="photoTone" cx="0.62" cy="0.62" r="0.75">
      <stop offset="0" stop-color="#1f7f9c"/>
      <stop offset=".25" stop-color="#1a4e72"/>
      <stop offset=".6" stop-color="#142c4f"/>
      <stop offset="1" stop-color="#0a1830"/>
    </radialGradient>
    <linearGradient id="tileTax" x1="0" y1="0" x2="1" y2="1">
      <stop offset="0" stop-color="#c9d9ea"/><stop offset="1" stop-color="#4d77a6"/>
    </linearGradient>
    <linearGradient id="tileLabor" x1="0" y1="0" x2="1" y2="1">
      <stop offset="0" stop-color="#cfe3f3"/><stop offset=".6" stop-color="#d9975a"/><stop offset="1" stop-color="#5c5a62"/>
    </linearGradient>
    <linearGradient id="tileAccounting" x1="0" y1="0" x2="0" y2="1">
      <stop offset="0" stop-color="#eef1f5"/><stop offset="1" stop-color="#4a4f59"/>
    </linearGradient>
    <linearGradient id="tileAdmin" x1="0" y1="0" x2="1" y2="1">
      <stop offset="0" stop-color="#b9c8d6"/><stop offset="1" stop-color="#5b6778"/>
    </linearGradient>
    <linearGradient id="tileFinance" x1="0" y1="0" x2="1" y2="1">
      <stop offset="0" stop-color="#f0eaf5"/><stop offset="1" stop-color="#9a9ed4"/>
    </linearGradient>
    <clipPath id="coverClip"><rect x="0" y="0" width="1200" height="444" rx="8"/></clipPath>
  </defs>

  <g class="cover" transform="translate(0,100)" clip-path="url(#coverClip)">
    <rect class="cover-bg" width="1200" height="444" fill="url(#coverBlue)"/>

    <path class="cover-photo" role="img" aria-label="Businessman in a dark suit holding a tablet with a glowing rising stock chart above it"
          d="M0 0 H482 C560 90 575 300 377 444 H0 Z" fill="url(#photoTone)"/>
    <path class="cover-curve" d="M482 0 C560 90 575 300 377 444" fill="none" stroke="var(--brand-mid)" stroke-width="10"/>
    <path d="M494 0 C574 92 588 305 392 444" fill="none" stroke="var(--brand-light)" stroke-width="2" opacity=".6"/>

    <polygon class="logo-panel" points="0,0 338,0 90,143 0,85" fill="var(--white)"/>
    <rect x="14" y="16" width="32" height="32" fill="var(--brand-blue)"/>
    <text class="brand-name" x="54" y="42" font-size="24">Velarte9</text>
    <text class="brand-tagline" x="55" y="57" font-size="7.5">ASESORÍA Y ADMINISTRACIÓN</text>
    <text class="brand-tagline" x="55" y="67" font-size="7.5">DE EMPRESAS</text>

    <text class="headline" x="862" y="88" text-anchor="middle" fill="var(--white)">SED EU <tspan class="accent">ORCI</tspan> <tspan class="light">ENIM</tspan></text>
    <text class="lead" x="862" y="113" text-anchor="middle">Nullam eget dolor nec risus commodo scelerisque eget ut sem. Nunc et</text>
    <text class="lead" x="862" y="137" text-anchor="middle">odio a ligula ornare aliquam vitae at purus.</text>

    <g class="phone-icon" transform="translate(727,175)">
      <circle r="15" fill="none" stroke="var(--white)" stroke-width="2"/>
      <path d="M-5 -6 l3 -1 2 4 -2 2 c1 2 3 4 5 5 l2 -2 4 2 -1 3 c-7 1 -14 -6 -13 -13z" fill="var(--white)"/>
    </g>
    <text class="phone-number" x="750" y="185">600 123 456</text>

    <g class="services">
      <g transform="translate(559,209)">
        <rect width="116" height="112" rx="18" fill="var(--brand-light)"/>
        <rect x="3" y="3" width="110" height="106" rx="16" fill="url(#tileTax)" role="img" aria-label="Tax documents with large TAX letters"/>
      </g>
      <g transform="translate(684,209)">
        <rect width="116" height="112" rx="18" fill="var(--brand-light)"/>
        <rect x="3" y="3" width="110" height="106" rx="16" fill="url(#tileLabor)" role="img" aria-label="Construction worker in a hard hat and safety vest"/>
      </g>
      <g transform="translate(808,209)">
        <rect width="116" height="112" rx="18" fill="var(--brand-light)"/>
        <rect x="3" y="3" width="110" height="106" rx="16" fill="url(#tileAccounting)" role="img" aria-label="Hand with pen over a calculator and papers"/>
      </g>
      <g transform="translate(932,209)">
        <rect width="116" height="112" rx="18" fill="var(--brand-light)"/>
        <rect x="3" y="3" width="110" height="106" rx="16" fill="url(#tileAdmin)" role="img" aria-label="Administrator in a grey suit in an office"/>
      </g>
      <g transform="translate(1056,209)">
        <rect width="116" height="112" rx="18" fill="var(--brand-light)"/>
        <rect x="3" y="3" width="110" height="106" rx="16" fill="url(#tileFinance)" role="img" aria-label="Financial charts on a laptop and phone"/>
      </g>
      <text class="service-label" x="617" y="345" text-anchor="middle">TAX</text>
      <text class="service-label" x="742" y="345" text-anchor="middle">LABOR</text>
      <text class="service-label" x="866" y="345" text-anchor="middle">ACCOUNTING</text>
      <text class="service-label" x="990" y="345" text-anchor="middle">ADMINISTRATION</text>
      <text class="service-label" x="1114" y="345" text-anchor="middle">FINANCIAL</text>
    </g>

    <polygon class="contact-band" points="600,387 1200,387 1200,444 545,444" fill="var(--white)"/>
    <rect x="545" y="439" width="655" height="5" fill="var(--brand-mid)"/>
    <g class="icon-mail" transform="translate(610,402)" fill="none" stroke="var(--brand-blue)" stroke-width="1.6">
      <rect width="24" height="17" rx="1"/>
      <path d="M0 0 L12 9 L24 0"/>
    </g>
    <text class="contact-text" x="641" y="418">INFO@VELARTE9.COM</text>
    <g class="icon-globe" transform="translate(930,410)" fill="none" stroke="var(--brand-blue)" stroke-width="1.5">
      <circle r="11"/>
      <ellipse rx="5" ry="11"/>
      <path d="M-11 0 H11 M-9 -6 H9 M-9 6 H9"/>
    </g>
    <text class="contact-text" x="950" y="418">WWW.VELARTE9.COM</text>
  </g>

  <g class="profile" transform="translate(126,596)">
    <circle r="70" fill="var(--white)" stroke="var(--brand-mist)" stroke-width="4"/>
    <rect x="-46" y="-14" width="14" height="14" fill="var(--brand-blue)"/>
    <text class="brand-name" x="-28" y="-1" font-size="17">Velarte9</text>
    <text class="brand-tagline" x="-28" y="9" font-size="5">ASESORÍA Y ADMINISTRACIÓN</text>
    <text class="brand-tagline" x="-28" y="16" font-size="5">DE EMPRESAS</text>
  </g>
</svg>
</body>
</html>
```